Geschäftspapiere für Rechtsanwaltskanzlei
Zielgruppe
Rechtsanwaltskanzlei mit dem Spezialgebiet Urheber-/Medienrecht; Mandanten sind Urheber, insbesondere von Musik- und Filmwerken, sowie Unternehmen, deren Unternehmenszweck die Herstellung- und Verwertung vorstehender Werke ist (z.B. Verlage, Filmproduktionsunternehmen). Das Design soll seriös sein, dabei aber einen modernen Touch haben.
Aufgabenstellung
Das Design muss im schwarz-weiß Ausdruck gut lesbar sein.
Es sollen folgende Informationen enthalten sein
Rechtsanwaltskanzlei Brunsmann
Rechtsanwältin Helga Brunsmann, MBA
Wiesenhang 27
14059 Berlin
Helga.Brunsmann@ra-brunsmann.com
Tel: +491524718260

```html
<!DOCTYPE html>
<html lang="de">
<head>
<meta charset="utf-8">
<title>Briefbogen – Rechtsanwaltskanzlei Brunsmann</title>
<link rel="stylesheet" href="https://fonts.googleapis.com/css2?family=Inter:wght@400;600&display=swap">
<style>
  :root {
    --backdrop: #b3b3b3;
    --paper: #ffffff;
    --ink: #222222;
    --ink-strong: #333333;
    --gold: #bf9f6b;
    --fold: #cfcfcf;
  }
  * { margin: 0; padding: 0; box-sizing: border-box; }
  html, body {
    width: 1200px;
    height: 1200px;
    overflow: hidden;
    background: var(--backdrop);
    font-family: "Inter", Helvetica, Arial, sans-serif;
  }
  .letterhead {
    position: absolute;
    left: 175px;
    top: 0;
    width: 849px;
    height: 1200px;
    background: var(--paper);
    color: var(--ink);
  }
  .brand {
    position: absolute;
    left: 0;
    width: 798px;
    top: 54px;
    text-align: center;
  }
  .brand-name {
    display: block;
    font-weight: 600;
    font-size: 34px;
    line-height: 40px;
    letter-spacing: 0.5px;
    color: var(--ink-strong);
  }
  .brand-type {
    display: block;
    font-weight: 400;
    font-size: 20px;
    line-height: 24px;
    letter-spacing: 0.6px;
    color: var(--gold);
  }
  .return-address {
    position: absolute;
    left: 168px;
    top: 201px;
    font-size: 12px;
    line-height: 16px;
  }
  .contact {
    position: absolute;
    left: 590px;
    top: 171px;
    font-size: 12px;
    line-height: 14px;
    font-style: normal;
  }
  .contact p { margin-bottom: 7px; }
  .contact .street { margin-bottom: 0; }
  .contact .city { margin-bottom: 12px; }
  .contact .mail { margin-bottom: 8px; }
  .contact-tab {
    position: absolute;
    right: 0;
    top: 174px;
    width: 16px;
    height: 95px;
    background: var(--gold);
  }
  .fold-mark {
    position: absolute;
    height: 1px;
    background: var(--fold);
  }
  .fold-mark.upper { left: 18px; top: 402px; width: 21px; }
  .fold-mark.center { left: 25px; top: 600px; width: 38px; }
  .fold-mark.lower { left: 18px; top: 805px; width: 21px; }
  .footer-band {
    position: absolute;
    left: 0;
    right: 0;
    top: 1165px;
    height: 12px;
    background: var(--gold);
  }
</style>
</head>
<body>
  <main class="letterhead">
    <header class="brand">
      <span class="brand-name">BRUNSMANN</span>
      <span class="brand-type">RECHTSANWALTSKANZLEI</span>
    </header>

    <p class="return-address">Wiesenhang 27 | 14059 Berlin</p>

    <address class="contact">
      <p>Rechtsanwältin Helga Brunsmann, MBA</p>
      <p class="street">Wiesenhang 27</p>
      <p class="city">14059 Berlin</p>
      <p class="mail">E-mail:Helga.Brunsmann@ra-brunsmann.com</p>
      <p>Tel: +491524718260</p>
    </address>
    <div class="contact-tab"></div>

    <div class="fold-mark upper"></div>
    <div class="fold-mark center"></div>
    <div class="fold-mark lower"></div>

    <div class="footer-band"></div>
  </main>
</body>
</html>
```